Package updated look

Hello, we want to change all our product labels, we want to start with this line of vinegars and oyster sauce. the bottles are a clear pet and red cap. there are picture of our current vinegar and soy sauce in www.dorvalepantry.com

Target Market(s)

General market

Requirements
Must have
• must be bilingual english and spanish

```html
<!DOCTYPE html>
<html lang="es">
<head>
<meta charset="utf-8">
<title>Salsa Ostion – Oyster Sauce label</title>
<link rel="stylesheet" href="https://fonts.googleapis.com/css2?family=Montserrat:wght@400;600;800;900&family=Cabin:wght@400;600;700&family=Noto+Sans+SC:wght@700&display=swap">
<style>
:root{
  --label-red:#d32f3a;
  --deep-red:#b81f2b;
  --box-red:#e2262c;
  --sun-yellow:#f6e21e;
  --panel-yellow:#f7e63a;
  --ink:#1f1f1f;
  --panel-dark:#262626;
  --white:#ffffff;
  --chili:#d9151b;
  --gold:#e8b820;
}
*{box-sizing:border-box;margin:0;padding:0}
html,body{width:1200px;height:700px;overflow:hidden;background:var(--white)}
.canvas{position:relative;width:1200px;height:700px;background:var(--white)}
.label{position:absolute;left:20px;top:117px;width:1130px;height:455px;transform:scale(1.0265);transform-origin:0 0;background:var(--label-red);font-family:"Cabin",sans-serif;color:var(--white);overflow:hidden}
.trim-band{position:absolute;left:0;width:100%;height:23px;background:var(--sun-yellow);border-top:4px solid var(--deep-red);border-bottom:4px solid var(--deep-red)}
.trim-band.top{top:7px}
.trim-band.bottom{top:427px}
.info-col{position:absolute;width:145px}
.info-col.es{left:18px}
.info-col.en{left:170px}
.ingredients-block{top:44px}
.instructions-block{top:157px}
.box-head{background:var(--ink);font-family:"Montserrat",sans-serif;font-weight:800;font-size:8.5px;line-height:10px;padding:1px 14px;height:23px;display:flex;align-items:center;text-transform:uppercase;letter-spacing:.3px}
.box-body{background:var(--box-red);padding:6px 14px;font-size:8px;line-height:10.4px}
.box-body .sub{font-family:"Montserrat",sans-serif;font-weight:800;color:var(--sun-yellow);font-size:8px;text-transform:uppercase;margin-bottom:6px}
.ingredients{height:85px}
.instructions{height:145px;border-radius:0 0 10px 10px;padding-top:10px}
.barcode-area{position:absolute;left:18px;top:342px;width:145px;height:66px;background:var(--white);border-radius:10px;display:flex;align-items:center;justify-content:center;font-family:"Montserrat",sans-serif;font-weight:800;font-size:7.5px;color:var(--chili);letter-spacing:.4px}
.net-weight{position:absolute;left:183px;top:364px;font-family:"Montserrat",sans-serif;font-weight:800;font-size:8px;line-height:10px}
.partner-badge{position:absolute;border-radius:50%}
.partner-badge.country{left:426px;top:80px;width:68px;height:46px;background:var(--chili);border:2px solid var(--white)}
.partner-badge.importer{left:676px;top:80px;width:60px;height:52px;background:var(--ink);border:2px solid var(--white)}
.mascot{position:absolute;left:542px;top:76px;width:96px;height:82px;border-radius:48px 48px 8px 8px;background:radial-gradient(circle at 50% 40%,var(--sun-yellow),var(--gold));border:3px solid var(--white)}
.brand-name{position:absolute;left:400px;top:160px;width:380px;text-align:center;font-family:"Montserrat",sans-serif;font-weight:900;font-size:42px;line-height:44px;color:var(--white);letter-spacing:1px}
.tagline{position:absolute;left:440px;top:210px;width:300px;text-align:center;font-family:"Noto Sans SC",sans-serif;font-weight:700;font-size:25px;line-height:32px;letter-spacing:3px;color:var(--sun-yellow)}
.chili{position:absolute;left:532px;top:266px;width:122px;height:58px;border-radius:50% 60% 40% 70%/60% 50% 50% 40%;background:linear-gradient(160deg,#3fa33a 0 14%,var(--chili) 15% 100%);transform:rotate(-12deg)}
.product-name{position:absolute;left:385px;top:322px;width:410px;text-align:center;font-family:"Montserrat",sans-serif;font-weight:900;font-size:48px;line-height:52px;color:var(--chili);-webkit-text-stroke:2px var(--white);paint-order:stroke fill;letter-spacing:-.5px}
.product-sub{position:absolute;left:385px;top:367px;width:410px;text-align:center;font-family:"Montserrat",sans-serif;font-weight:900;font-size:28px;line-height:30px;color:var(--sun-yellow);-webkit-text-stroke:1.5px var(--chili);paint-order:stroke fill}
.nutrition{position:absolute;left:840px;top:45px;width:290px;height:285px;background:linear-gradient(90deg,var(--panel-yellow) 70%,#efd82a);color:var(--ink);padding:7px 10px;border-radius:10px 0 0 0}
.nutrition h2{font-family:"Montserrat",sans-serif;font-weight:800;font-size:10.5px;color:var(--chili);letter-spacing:.3px}
.nutrition .small{font-size:6.5px;line-height:9px}
.nutrition hr{border:0;border-top:1px solid var(--ink);margin:4px 0}
.cal-row{display:flex;justify-content:space-between;font-family:"Montserrat",sans-serif;font-weight:600;font-size:18px;line-height:22px;border-bottom:2px solid var(--ink);padding-bottom:1px}
.dv{font-size:6px;color:var(--chili)}
.nut-list{list-style:none;margin-top:10px;padding-left:10px}
.nut-list li{display:flex;justify-content:space-between;font-size:6.5px;line-height:10.4px}
.vitamins{display:grid;grid-template-columns:1fr 1fr;gap:0 24px;margin-top:14px;font-size:6.3px;line-height:9px}
.vitamins span{display:flex;justify-content:space-between}
.footnote{font-size:6px;line-height:8.5px;margin-top:22px}
.distributor{position:absolute;left:840px;top:330px;width:290px;height:85px;background:var(--panel-dark);border-radius:0 0 0 10px;padding:10px 10px 0 20px;display:grid;grid-template-columns:120px 1fr;gap:0 10px;font-size:6.3px;line-height:9px;color:#e6e6e6}
.distributor .origin{position:absolute;right:12px;bottom:6px;color:#bbb}
.distributor .origin::before{content:"";display:inline-block;width:90px;border-top:1px solid #888;vertical-align:middle;margin-right:4px}
</style>
</head>
<body>
<div class="canvas">
  <section class="label">
    <div class="trim-band top" role="img" aria-label="Yellow zigzag pattern band"></div>

    <div class="info-col es ingredients-block">
      <h3 class="box-head">Vegetales saltados con sillau</h3>
      <div class="box-body ingredients">
        <p class="sub">Ingredientes</p>
        <p>Salsa ostion<br>Salsa de soja<br>Azucar<br>Jengibre<br>Agua</p>
      </div>
    </div>
    <div class="info-col en ingredients-block">
      <h3 class="box-head">Sauteed vegetables with soy sauce</h3>
      <div class="box-body ingredients">
        <p class="sub">Ingredient</p>
        <p>Oyster sauce<br>Soy sauce<br>Sugar<br>Ginger<br>Water</p>
      </div>
    </div>

    <div class="info-col es instructions-block">
      <h3 class="box-head">Instrucciones</h3>
      <div class="box-body instructions">Calentar el work a fuego medio, anadir aceite, brocoli, ajo y agua, saltear aprox. 1 min. Agregar zanahoria, arvejita china, hongos y kion; saltear hasta que este listo. En un bol pequeno coloque el sillau, caldo de pollo y chuno, disuelva bein, anadir al work y mover aprox1 min. Acompane con arroz.</div>
    </div>
    <div class="info-col en instructions-block">
      <h3 class="box-head">Instrucciones</h3>
      <div class="box-body instructions">Heat wok over medium heat, add the oil, broccoli, garlic and water, stir-fry for 1 min. Add carrots, snow peas, mushroom, and ginger; stir-fry until done. in small bowl, combine the soy sauce, broth and corn starch; mix well to dissolve. Add to work and stir constantly for about 1 minute. Accompanied with rice.</div>
    </div>

    <div class="barcode-area">CODIGO DE BARRAS</div>
    <p class="net-weight">Net weight/Peso<br>neto 16.9 fl oz (500 ml)</p>

    <div class="partner-badge country" role="img" aria-label="Country brand badge"></div>
    <div class="partner-badge importer" role="img" aria-label="Importer badge"></div>
    <div class="mascot" role="img" aria-label="Golden Andean idol mascot illustration"></div>
    <h1 class="brand-name">Dorvale Pantry</h1>
    <p class="tagline">好的 最好的</p>

    <div class="chili" role="img" aria-label="Red chili pepper illustration"></div>
    <h2 class="product-name">SALSA OSTION</h2>
    <p class="product-sub">OYSTER SAUCE</p>

    <div class="nutrition">
      <h2>NUTRITION FACTS/DATOS DE NUTRCION</h2>
      <p class="small">por porcion 5gms</p>
      <hr>
      <p class="small">Amount per serving/Cantidad por racion</p>
      <div class="cal-row"><span>Calories/Calorias</span><span>7</span></div>
      <p class="dv">% Daily Value*/Valor diario*</p>
      <ul class="nut-list">
        <li><span>Total Fat/Grasa total 0g</span><span>0%</span></li>
        <li><span>Saturated fat/Grasa saturada 0g</span><span>0%</span></li>
        <li><span>Trans fat/Grasa Trans 0g</span><span></span></li>
        <li><span>Cholestrol/Colestrol 0mg</span><span>0%</span></li>
        <li><span>Sodium/Sodio 300mg</span><span>39%</span></li>
        <li><span>Total Carbohydrate/Carbohidrato total 1.5g</span><span>0%</span></li>
        <li><span>Dietary Fiber/Fibra Dietetica 0g</span><span>0%</span></li>
        <li><span>Total Sugars/Azucares Total 1g</span><span></span></li>
        <li><span>Includes 0.3g Added Sugars/Incluye 0.3g azucares anadidos</span><span>1%</span></li>
        <li><span>Protein/Proteinas 0g</span><span></span></li>
      </ul>
      <div class="vitamins">
        <span><span>Vitamin D/Vitamina D 0mcg</span><span>0%</span></span>
        <span><span>Iron/Hierro 0.1mg</span><span>0%</span></span>
        <span><span>Calcium/calcio 5mg</span><span>0%</span></span>
        <span><span>Potasium/Potasio 16mg</span><span>0%</span></span>
      </div>
      <p class="footnote">*The % daily value (DV) tells you who much a nutrient in a serving of food contributes to a daily diet 2000 calories a day is used for general nutrition advice</p>
    </div>

    <div class="distributor">
      <p>Imported and distributed by:<br>Andes Bay Trading Inc<br>RIVERTON,N.J 08077 - USA<br>Phone: (555) 014-2290<br>Fax: (555) 014-2291<br>www.andesbaytrading.com</p>
      <p>Conservar en lugar fresco y seco. Contiene soya y trigo. Alerta alergia alimentaria.<br><br>Keep in a fresh and dry place. Contains soy and wheat. Food Allergy Warning.</p>
      <p class="origin">Product Of Peru</p>
    </div>

    <div class="trim-band bottom" role="img" aria-label="Yellow zigzag pattern band"></div>
  </section>
</div>
</body>
</html>
```